Looking for a dynamic business card for a pizzeria.

A business card with our food, logo, and space for name, title, email, website, phone. The card should convey quality, unique, amazing. On the front, I envision food photo or photos with the owners names and contact information. On the back, more food with locations, website, facebook, twitter, instagram icons. It should look polished, not cartoonish, or plain.
Target Market(s)
upscale, local food buyers, 30-50 years in age.
Industry/Entity Type
Restaurant
Contact Information for Business Card
Business Name: Crustella, LLC
Website: www.crustellaovens.com
Back:
2 locations: (can list on the back of card)
1. NORTHGATE
2736 Marlow Street
Larkhaven, OR 97455
360-555-0143
2. CEDAR RIDGE
1187 Pelham Street
Larkhaven, OR 97458
360-555-0187
front:
EDITABLE space for
Business name
Person's Name
title
2nd title
Email address
cell-phone number
Requirements
Must have
- logo
- my food photo or photos (no watermarks showing)
- locations on back
- Person contact information on front
- full bleed

```html
<!DOCTYPE html>
<html lang="en">
<head>
<meta charset="utf-8">
<title>Crustella Business Card</title>
<link href="https://fonts.googleapis.com/css2?family=Questrial&family=Mulish:wght@700;800&display=swap" rel="stylesheet">
<style>
  :root {
    --green: #1f4a1f;
    --red: #b3181f;
    --charcoal: #2f2f2f;
    --ink: #2a2a2a;
    --paper: #ffffff;
    --backdrop: #ece6dc;
  }
  * { box-sizing: border-box; margin: 0; padding: 0; }
  html, body { width: 1189px; height: 1200px; overflow: hidden; }
  body {
    background: var(--backdrop);
    font-family: "Questrial", "Century Gothic", sans-serif;
    color: var(--ink);
    position: relative;
  }
  .card {
    position: absolute;
    left: 171px;
    width: 856px;
    height: 488px;
    background: var(--paper);
    overflow: hidden;
  }
  .card--front { top: 67px; }
  .card--back { top: 626px; }

  .brand {
    position: absolute;
    display: flex;
    align-items: center;
    gap: 16px;
    color: var(--green);
    font-size: 68px;
    letter-spacing: 1px;
  }
  .brand__dot {
    width: 26px; height: 26px;
    border-radius: 50%;
    background: var(--red);
  }
  .card--front .brand { left: 45px; top: 60px; }
  .card--back .brand { left: 61px; top: 92px; }

  .person {
    position: absolute;
    right: 68px;
    top: 64px;
    text-align: right;
  }
  .person__name {
    font-family: "Mulish", Verdana, sans-serif;
    font-weight: 800;
    font-size: 39px;
    color: var(--green);
    line-height: 1;
  }
  .person__title {
    font-size: 27px;
    color: var(--red);
    line-height: 1;
    margin-top: 0;
  }

  .rule { position: absolute; left: 0; width: 100%; background: var(--charcoal); }
  .rule--top-thick { top: 184px; height: 8px; }
  .rule--top-thin { top: 195px; height: 4px; }
  .rule--bottom-thin { top: 411px; height: 4px; }

  .gallery {
    position: absolute;
    top: 204px; left: 0;
    width: 100%; height: 202px;
    display: grid;
    grid-template-columns: repeat(4, 1fr);
    gap: 6px;
    background: var(--charcoal);
  }
  .gallery__photo { height: 100%; }
  .gallery__photo--sandwich { background: linear-gradient(135deg, #6b4a2a, #c99a45 55%, #4f6b2a); }
  .gallery__photo--oven { background: linear-gradient(180deg, #e09a3a, #a4451f 45%, #d9c3a8); }
  .gallery__photo--topping { background: linear-gradient(160deg, #4a3a33, #d98b6c 45%, #e8d2bd); }
  .gallery__photo--salad { background: linear-gradient(135deg, #e7d27a, #7fae3a 45%, #5a2e24); }

  .contact-bar {
    position: absolute;
    top: 420px; left: 0;
    width: 100%; height: 68px;
    background: var(--charcoal);
    color: #fff;
    font-size: 26px;
  }
  .contact-bar__item {
    position: absolute;
    top: 19px;
    display: flex;
    align-items: center;
    gap: 20px;
  }
  .contact-bar__item--email { left: 46px; }
  .contact-bar__item--phone { left: 429px; }
  .contact-bar svg { display: block; }

  .social {
    position: absolute;
    left: 650px; top: 73px;
    display: flex;
    gap: 20px;
  }
  .social__tile { width: 35px; height: 35px; border-radius: 2px; }
  .social__tile--a { background: #3b5998; }
  .social__tile--b { background: #2a9fd8; }
  .social__tile--c { background: #1d4e6e; }

  .location { position: absolute; top: 296px; }
  .location--north { left: 60px; }
  .location--cedar { left: 501px; }
  .location__name {
    font-family: "Mulish", Verdana, sans-serif;
    font-weight: 800;
    font-size: 26px;
    line-height: 1;
    color: var(--green);
    letter-spacing: -0.3px;
    margin-bottom: 24px;
  }
  .location__address { font-size: 28px; line-height: 29px; }
  .location__phone {
    font-family: "Mulish", Verdana, sans-serif;
    font-weight: 700;
    font-size: 26px;
    margin-top: 8px;
  }
</style>
</head>
<body>
  <section class="card card--front">
    <div class="brand"><span class="brand__name">Crustella</span><span class="brand__dot"></span></div>
    <div class="person">
      <div class="person__name">Employee Name</div>
      <div class="person__title">Managing Director</div>
    </div>
    <div class="rule rule--top-thick"></div>
    <div class="rule rule--top-thin"></div>
    <div class="gallery">
      <div class="gallery__photo gallery__photo--sandwich" role="img" aria-label="Photo of a grilled panini sandwich with greens"></div>
      <div class="gallery__photo gallery__photo--oven" role="img" aria-label="Photo of pizza rolls baking in a fired oven"></div>
      <div class="gallery__photo gallery__photo--topping" role="img" aria-label="Photo of a hand placing pepperoni on pizza dough"></div>
      <div class="gallery__photo gallery__photo--salad" role="img" aria-label="Photo of sliced beef with peppers and red onion"></div>
    </div>
    <div class="rule rule--bottom-thin"></div>
    <div class="contact-bar">
      <div class="contact-bar__item contact-bar__item--email">
        <svg width="26" height="26" viewBox="0 0 26 26" aria-hidden="true">
          <rect x="0" y="0" width="26" height="26" fill="#fff"/>
          <rect x="4" y="7" width="18" height="12" fill="none" stroke="#2f2f2f" stroke-width="1.6"/>
          <path d="M4 7 L13 14 L22 7 M4 19 L11 12.5 M22 19 L15 12.5" fill="none" stroke="#2f2f2f" stroke-width="1.4"/>
        </svg>
        <span>you@crustellaovens.com</span>
      </div>
      <div class="contact-bar__item contact-bar__item--phone">
        <svg width="26" height="26" viewBox="0 0 26 26" aria-hidden="true">
          <rect x="0" y="0" width="26" height="26" fill="#fff"/>
          <rect x="8" y="4" width="10" height="18" rx="1.5" fill="#2f2f2f"/>
          <rect x="10" y="6" width="6" height="5" fill="#fff"/>
          <rect x="10" y="13" width="6" height="7" fill="#bbb"/>
        </svg>
        <span>123 456 7890</span>
      </div>
    </div>
  </section>

  <section class="card card--back">
    <div class="brand"><span class="brand__name">Crustella</span><span class="brand__dot"></span></div>
    <div class="social" aria-label="Social media">
      <span class="social__tile social__tile--a"></span>
      <span class="social__tile social__tile--b"></span>
      <span class="social__tile social__tile--c"></span>
    </div>
    <div class="location location--north">
      <div class="location__name">NORTHGATE</div>
      <div class="location__address">2736 Marlow Street<br>Larkhaven, OR 97455</div>
      <div class="location__phone">360-555-0143</div>
    </div>
    <div class="location location--cedar">
      <div class="location__name">CEDAR RIDGE</div>
      <div class="location__address">1187 Pelham Street<br>Larkhaven, OR 97458</div>
      <div class="location__phone">360-555-0187</div>
    </div>
  </section>
</body>
</html>
```